Wall Word Art for tree care company to brand core values at the business

I am looking to have some wall art designed base on our companies core values and passion to be displayed around our office walls.

1. Grow and develop our team to win
2. competitive - value in a goal and purpose. not just about winning...its about the process. Iron sharpens Iron
3. Open & Honest - sharing the storyline. yes is our yes. no is our no. vulnerable.
4. Accountable - celebrating the wins & addressing the opportunities. hold each other to a standard, with grace.
5. Professional - a pro's-pro. how we communicate, look and act.
6. Growing Relationships through trees.

Target Market(s)

our employees

Industry/Entity Type

tree care

Font styles to use
Other font styles liked:
• montserrat

Requirements
Must have
• brand colors and font
Nice to have
• incorporate icons and logo, or create new icons

```html
<!DOCTYPE html>
<html lang="en">
<head>
<meta charset="UTF-8">
<title>ALDEN Tree Care – Core Values</title>
<link href="https://fonts.googleapis.com/css2?family=Montserrat:wght@400;800&display=swap" rel="stylesheet">
<style>
  :root {
    --brand-red: #c8202f;
    --accent-orange: #e87722;
    --blush: #f2c6cb;
    --mist: #fbeef0;
    --ink: #1c1c1c;
    --paper: #ffffff;
    --icon-fill: #fdf1e7;
  }
  * { margin: 0; padding: 0; box-sizing: border-box; }
  html, body { width: 927px; height: 1200px; overflow: hidden; background: var(--paper); }
  .poster {
    position: relative;
    width: 927px;
    height: 1200px;
    overflow: hidden;
    background: var(--paper);
    font-family: "Montserrat", sans-serif;
    color: var(--ink);
  }
  .top-band { position: absolute; top: 0; left: 0; width: 100%; height: 41px; background: var(--brand-red); }
  .cloud-scene {
    position: absolute; left: 0; bottom: 0; width: 100%; height: 320px;
    background: linear-gradient(to bottom, rgba(251,238,240,0) 0%, var(--mist) 18%, var(--blush) 45%, var(--blush) 58%, var(--brand-red) 72%, var(--brand-red) 100%);
  }
  .value-track { position: absolute; top: 0; left: 0; }
  .brand-name {
    position: absolute; left: 510px; top: 117px;
    color: var(--brand-red); font-weight: 800; font-size: 32px;
    line-height: 1; letter-spacing: 0.5px; white-space: nowrap;
  }
  .value { position: absolute; }
  .value--left { left: 266px; text-align: left; }
  .value--right { text-align: right; }
  .value-title {
    color: var(--brand-red); font-weight: 800; font-size: 35px;
    line-height: 40px; letter-spacing: 0.5px;
  }
  .value-title .lead { font-weight: 400; font-size: 21px; color: var(--ink); letter-spacing: 0.3px; }
  .value-text { font-size: 17px; line-height: 22px; margin-top: 4px; letter-spacing: 0.2px; }
</style>
</head>
<body>
<main class="poster">
  <div class="top-band"></div>
  <div class="cloud-scene" role="img" aria-label="Soft layered pink and red clouds along the bottom edge"></div>

  <svg class="value-track" width="927" height="1200" viewBox="0 0 927 1200">
    <g fill="none" stroke="var(--brand-red)" stroke-width="8" stroke-linecap="round">
      <line x1="152" y1="133.5" x2="489" y2="133.5"/>
      <line x1="152" y1="302.5" x2="775" y2="302.5"/>
      <line x1="152" y1="471.5" x2="775" y2="471.5"/>
      <line x1="152" y1="640.5" x2="775" y2="640.5"/>
      <line x1="152" y1="809.5" x2="775" y2="809.5"/>
      <line x1="152" y1="978.5" x2="741" y2="978.5"/>
    </g>
    <g class="value-badges" fill="var(--paper)" stroke="var(--brand-red)" stroke-width="12">
      <circle cx="152" cy="218" r="84"/>
      <circle cx="775" cy="387" r="84"/>
      <circle cx="152" cy="556" r="84"/>
      <circle cx="775" cy="725" r="84"/>
      <circle cx="152" cy="894" r="84"/>
    </g>
    <g class="value-icons" stroke="var(--accent-orange)" stroke-width="2" fill="var(--icon-fill)">
      <circle cx="152" cy="218" r="71" role="img" aria-label="Icon of a team beside a rising bar chart"/>
      <circle cx="775" cy="387" r="71" role="img" aria-label="Icon of two fists bumping"/>
      <circle cx="152" cy="556" r="71" role="img" aria-label="Icon of a handshake under a star"/>
      <circle cx="775" cy="725" r="71" role="img" aria-label="Icon of a clipboard with a rising bar chart"/>
      <circle cx="152" cy="894" r="71" role="img" aria-label="Icon of three professionals in ties"/>
    </g>
  </svg>

  <p class="brand-name">ALDEN TREE CARE</p>

  <section class="value value--left" style="top:178px;">
    <h2 class="value-title">GROW AND<br>DEVELOP <span class="lead">our team to win</span></h2>
  </section>

  <section class="value value--right" style="top:330px; right:316px;">
    <h2 class="value-title">COMPETITIVE</h2>
    <p class="value-text">Value in a goal and purpose.<br>not just about winning...<br>its about the process. Iron sharpens Iron</p>
  </section>

  <section class="value value--left" style="top:510px;">
    <h2 class="value-title">OPEN &amp; HONEST</h2>
    <p class="value-text">Sharing the storyline.<br>yes is our yes. no is our no. vulnerable.</p>
  </section>

  <section class="value value--right" style="top:678px; right:274px;">
    <h2 class="value-title">ACCOUNTABLE</h2>
    <p class="value-text">Celebrating the wins &amp; addressing the opportunities.<br>hold each other to a standard, with grace.</p>
  </section>

  <section class="value value--left" style="top:859px;">
    <h2 class="value-title">PROFESSIONAL</h2>
    <p class="value-text">A pro's-pro. how we communicate, look and act.</p>
  </section>
</main>
</body>
</html>
```